Rural contractor needs professional informative business card

We need a business card design that looks professional but also includes information about the services that the business offers.
The business is an earthmoving and transport business. All of the services offered are listed on the old card attached.
The business is aimed at farmers so the design we are after is a classic look. The card needs to include all of the information that is listed on the old card design uploaded as an attachment. We recognize that this is a lot of information to fit on a business card but it also operates as a key marketing tool so is very important to the business.
Feel free to send me your questions.
Thanks
Reason: We are having trouble deciding between all these great designs - thank you for your efforts
We would love to see some designs using red with a little white and black. Also feel free to re-design our logo if you feel it needs to be to fit your designs. Thank you

```html
<!DOCTYPE html>
<html lang="en">
<head>
<meta charset="utf-8">
<title>Rourke Contracting – Business Card</title>
<link href="https://fonts.googleapis.com/css2?family=Jost:ital,wght@0,300;0,400;0,500;1,300&display=swap" rel="stylesheet">
<style>
  :root{
    --page:#ffffff;
    --card:#ffffff;
    --card-edge:#b9b9b9;
    --ink:#1e1e1e;
    --ink-soft:#3a3a3a;
    --corner:#9a9a9a;
    --faint:#b5b5b5;
    --sky-top:#3f86d6;
    --sky-low:#a9c9ea;
    --ground:#b9a58c;
    --field:#c9ab72;
    --dusk-top:#e8c9b4;
    --dusk-low:#8f7f6f;
  }
  *{box-sizing:border-box;margin:0;padding:0}
  html,body{width:1200px;height:905px;overflow:hidden;background:var(--page)}
  body{position:relative;font-family:"Jost",sans-serif;color:var(--ink)}

  .card{position:absolute;width:640px;height:365px;background:var(--card);border:1px solid var(--card-edge);overflow:hidden}
  .card--front{left:138px;top:86px}
  .card--back{left:510px;top:502px}

  .photo{position:absolute;width:252px;height:132px;border-radius:6px}
  .photo--truck{background:linear-gradient(180deg,var(--sky-top) 0%,var(--sky-low) 55%,var(--ground) 62%,var(--ground) 100%)}
  .photo--grader{background:linear-gradient(180deg,var(--sky-top) 0%,var(--sky-low) 45%,var(--field) 55%,#b89457 100%)}
  .photo--cotton{background:linear-gradient(180deg,var(--dusk-top) 0%,#d9cfc3 50%,var(--dusk-low) 70%,#6e6155 100%)}

  .brand{position:absolute;font-weight:500;font-size:25px;letter-spacing:.5px;white-space:nowrap;text-transform:uppercase}
  .brand__mark{display:inline-block;width:14px;height:14px;background:currentColor;margin-right:9px;vertical-align:1px}
  .card--front .brand{left:8px;top:171px;width:248px;text-align:center;color:var(--ink);font-size:23px}
  .card--front .brand-rule{position:absolute;left:8px;width:248px;height:2px;background:var(--ink)}
  .card--back .brand{left:252px;top:166px;width:160px;text-align:center;color:var(--faint);font-size:14px;letter-spacing:1px}

  .holder{position:absolute;right:86px;top:38px;font-weight:300;font-style:italic;font-size:28px;letter-spacing:.5px}
  .address,.contact{position:absolute;right:86px;text-align:right;font-weight:300;font-size:19px;line-height:25px}
  .address{top:122px}
  .contact{top:197px}
  .contact__line{display:flex;justify-content:flex-end;align-items:center;gap:5px}
  .contact__line--email{font-size:17px}
  .contact svg{flex:none}

  .tagline{position:absolute;left:272px;top:332px;font-weight:300;font-size:22px;letter-spacing:.3px}
  .tagline-rule{position:absolute;left:272px;top:364px;width:340px;height:2px;background:linear-gradient(90deg,transparent,#888 50%,transparent)}

  .corner{position:absolute;right:0;width:42px;height:42px;background:var(--corner)}
  .corner--top{top:0;clip-path:polygon(0 0,100% 0,100% 100%)}
  .corner--bottom{bottom:0;clip-path:polygon(100% 0,100% 100%,0 100%)}

  .service-head{position:absolute;top:163px;font-weight:400;font-size:23px;letter-spacing:.5px}
  .service-head--earth{left:17px}
  .service-head--transport{left:461px}
  .service-list{position:absolute;list-style:none;font-weight:300;font-size:23px;line-height:31px}
  .service-list--earth{left:14px;top:224px}
  .service-list--transport{left:455px;top:226px}
  .service-list li{display:flex;align-items:center;gap:9px}
</style>
</head>
<body>

<section class="card card--front" aria-label="Card front">
  <div class="photo photo--truck" style="left:5px;top:5px" role="img" aria-label="Photo of a white prime mover truck with flatbed trailer"></div>
  <div class="brand-rule" style="top:156px"></div>
  <div class="brand"><span class="brand__mark"></span>Rourke Contracting</div>
  <div class="brand-rule" style="top:207px"></div>
  <div class="photo photo--grader" style="left:5px;top:229px" role="img" aria-label="Photo of a yellow road grader in a harvested paddock"></div>

  <div class="corner corner--top"></div>
  <p class="holder">Callum Rourke</p>
  <p class="address">52 Tarrawong Street<br>Bellbrook 2899</p>
  <div class="contact">
    <p class="contact__line">
      <svg width="16" height="16" viewBox="0 0 24 24" aria-hidden="true"><path fill="#1e1e1e" d="M6.6 10.8a15.1 15.1 0 0 0 6.6 6.6l2.2-2.2c.3-.3.7-.4 1-.2 1.1.4 2.3.6 3.6.6.6 0 1 .4 1 1V20c0 .6-.4 1-1 1A17 17 0 0 1 3 4c0-.6.4-1 1-1h3.5c.6 0 1 .4 1 1 0 1.3.2 2.5.6 3.6.1.3 0 .7-.2 1z"/></svg>
      0400 555 172
    </p>
    <p class="contact__line contact__line--email">
      <svg width="15" height="11" viewBox="0 0 15 11" aria-hidden="true"><rect x=".6" y=".6" width="13.8" height="9.8" fill="none" stroke="#1e1e1e" stroke-width="1.2"/><path d="M.6.6l6.9 5.6L14.4.6M.6 10.4l5-4.4M14.4 10.4l-5-4.4" fill="none" stroke="#1e1e1e" stroke-width="1.1"/></svg>
      callumrourke@mailbox.net
    </p>
  </div>
  <p class="tagline">Earthmoving &amp; Transport Solutions</p>
  <div class="tagline-rule"></div>
  <div class="corner corner--bottom"></div>
</section>

<section class="card card--back" aria-label="Card back">
  <div class="photo photo--truck" style="left:5px;top:5px" role="img" aria-label="Photo of a white prime mover truck with flatbed trailer"></div>
  <div class="photo photo--cotton" style="left:390px;top:5px" role="img" aria-label="Photo of a truck carrying round cotton bales at dusk"></div>

  <h2 class="service-head service-head--earth">EARTHMOVING</h2>
  <div class="brand">Rourke Contracting</div>
  <h2 class="service-head service-head--transport">TRANSPORT</h2>

  <ul class="service-list service-list--earth">
    <li><svg width="12" height="10" viewBox="0 0 12 10" aria-hidden="true"><path d="M1 5.5l3 3L11 1" fill="none" stroke="#1e1e1e" stroke-width="2"/></svg>Road Building &amp; Maintenance</li>
    <li><svg width="12" height="10" viewBox="0 0 12 10" aria-hidden="true"><path d="M1 5.5l3 3L11 1" fill="none" stroke="#1e1e1e" stroke-width="2"/></svg>Poly Pipe Laying</li>
    <li><svg width="12" height="10" viewBox="0 0 12 10" aria-hidden="true"><path d="M1 5.5l3 3L11 1" fill="none" stroke="#1e1e1e" stroke-width="2"/></svg>Clearing Fence Lines</li>
    <li><svg width="12" height="10" viewBox="0 0 12 10" aria-hidden="true"><path d="M1 5.5l3 3L11 1" fill="none" stroke="#1e1e1e" stroke-width="2"/></svg>Sand &amp; Gravel Supplies</li>
  </ul>
  <ul class="service-list service-list--transport">
    <li><svg width="12" height="10" viewBox="0 0 12 10" aria-hidden="true"><path d="M1 5.5l3 3L11 1" fill="none" stroke="#1e1e1e" stroke-width="2"/></svg>Grain</li>
    <li><svg width="12" height="10" viewBox="0 0 12 10" aria-hidden="true"><path d="M1 5.5l3 3L11 1" fill="none" stroke="#1e1e1e" stroke-width="2"/></svg>Cotton</li>
    <li><svg width="12" height="10" viewBox="0 0 12 10" aria-hidden="true"><path d="M1 5.5l3 3L11 1" fill="none" stroke="#1e1e1e" stroke-width="2"/></svg>Sand &amp; Gravel</li>
    <li><svg width="12" height="10" viewBox="0 0 12 10" aria-hidden="true"><path d="M1 5.5l3 3L11 1" fill="none" stroke="#1e1e1e" stroke-width="2"/></svg>Wool</li>
  </ul>
</section>

</body>
</html>
```